4747 5858

Web(re)design of an existing directory search site www.le5858.be (in Dutch www.de4747.be and in English www.3737.be).

This site is a directory site, i.e. a "white pages" site whereby people can search the phone & details of another person based on a combination of name + city (for instance pellow in Brussels); one can also search a company also based on a combination of name + city (for instance Vornak in Brussels); last but not least one can also search the name of the subscriber behind a specific telephone number (also called reverse search).

This site is quite outdated and needs a redesign, see instructions.

We need the output in XD format.

```html
<!DOCTYPE html>
<html lang="fr">
<head>
<meta charset="utf-8">
<title>Les Renseignements CINQ-HUIT Utiles</title>
<link href="https://fonts.googleapis.com/css2?family=Roboto+Condensed:wght@300;400;700&family=Roboto:wght@400&display=swap" rel="stylesheet">
<style>
  :root {
    --red: #d90f16;
    --red-dark: #b50a10;
    --ink: #111111;
    --muted: #444444;
    --tab-bg: #ececec;
    --line: #bcbcbc;
    --white: #ffffff;
    --photo-a: #c9a57c;
    --photo-b: #6d4a36;
  }
  * { box-sizing: border-box; margin: 0; padding: 0; }
  html, body { width: 1200px; height: 600px; overflow: hidden; background: var(--white); }
  body { position: relative; font-family: "Roboto Condensed", Arial, sans-serif; color: var(--ink); }

  .brand { position: absolute; left: 171px; top: 40px; display: flex; align-items: center; gap: 8px; }
  .brand-dot { width: 14px; height: 14px; border-radius: 50%; background: var(--red); }
  .brand-name { font-weight: 700; font-size: 34px; color: var(--red); letter-spacing: 1px; }

  .headline { position: absolute; left: 0; width: 1200px; top: 45px; text-align: center; font-weight: 700; font-size: 27px; }
  .headline .accent { color: var(--red); }

  .lang { position: absolute; left: 953px; top: 52px; font-size: 18px; color: var(--muted); display: flex; align-items: center; gap: 5px; }
  .menu { position: absolute; left: 1015px; top: 56px; width: 23px; }
  .menu span { display: block; height: 2px; background: var(--ink); margin-bottom: 5px; }

  .tabs { position: absolute; top: 171px; left: 0; }
  .tab { position: absolute; top: 0; height: 31px; line-height: 31px; text-align: center; font-size: 16px; background: var(--tab-bg); color: #333; }
  .tab.is-active { background: var(--red); color: var(--white); }

  .field { position: absolute; width: 225px; height: 32px; border: 1px solid var(--line); padding-left: 13px; line-height: 30px; font-weight: 700; font-size: 13.5px; }
  .hint { position: absolute; font-weight: 300; font-size: 11px; color: #333; }

  .search-btn { position: absolute; left: 415px; top: 325px; width: 225px; height: 32px; background: linear-gradient(var(--red), var(--red-dark)); color: var(--white); display: flex; align-items: center; justify-content: center; gap: 10px; font-weight: 700; font-size: 14px; }

  .captcha { position: absolute; left: 170px; top: 412px; width: 224px; height: 54px; border: 1px solid #d3d3d3; background: #f9f9f9; font-family: Roboto, Arial, sans-serif; }
  .captcha-box { position: absolute; left: 8px; top: 16px; width: 20px; height: 20px; border: 2px solid #c1c1c1; border-radius: 2px; background: var(--white); }
  .captcha-label { position: absolute; left: 38px; top: 19px; font-size: 10.5px; color: #222; }
  .captcha-mark { position: absolute; right: 8px; top: 12px; width: 22px; height: 22px; border-radius: 50%; background: #9fb4d8; }
  .captcha-meta { position: absolute; right: 7px; top: 35px; text-align: center; font-size: 6px; color: #555; line-height: 8px; }

  .footer { position: absolute; left: 172px; top: 537px; font-size: 13.5px; color: #333; }
  .footer-links { display: flex; gap: 10px; }
  .footer-links .sep { color: #ccc; }
  .copyright { margin-top: 6px; }

  .hero { position: absolute; left: 0; top: 0; }
  .partner { position: absolute; left: 936px; top: 565px; display: flex; align-items: center; gap: 5px; font-size: 8px; font-weight: 700; color: var(--ink); }
  .partner-dot { width: 9px; height: 9px; border-radius: 50%; background: var(--red); }
</style>
</head>
<body>
  <header>
    <div class="brand"><span class="brand-dot"></span><span class="brand-name">58-58</span></div>
    <h1 class="headline">Les Renseignements <span class="accent">CINQ-HUIT</span> Utiles</h1>
    <div class="lang">FR
      <svg width="9" height="6" viewBox="0 0 9 6"><path d="M1 1l3.5 3.5L8 1" fill="none" stroke="#555" stroke-width="1.2"/></svg>
    </div>
    <div class="menu"><span></span><span></span><span></span></div>
  </header>

  <nav class="tabs">
    <div class="tab is-active" style="left:172px;width:102px">Particuliers</div>
    <div class="tab" style="left:278px;width:101px">Sociétés</div>
    <div class="tab" style="left:383px;width:138px">Annuaire inversé</div>
    <div class="tab" style="left:526px;width:107px">International</div>
  </nav>

  <form class="search">
    <div class="field" style="left:170px;top:241px">Nom de famille:</div>
    <div class="hint" style="left:177px;top:282px">Ex: Dupont, Janssens, ...</div>
    <div class="field" style="left:415px;top:241px">Localité:</div>
    <div class="hint" style="left:422px;top:282px">Ex: Liége, Anvers, 1150, ....</div>
    <div class="field" style="left:170px;top:325px">Prénom:</div>
    <div class="hint" style="left:177px;top:366px">Ex: Jan, Louis, ...</div>
    <div class="search-btn">
      <svg width="19" height="19" viewBox="0 0 19 19"><circle cx="8" cy="8" r="6.5" fill="none" stroke="#fff" stroke-width="1.3"/><path d="M12.8 12.8L18 18" stroke="#fff" stroke-width="1.3"/></svg>
      58-58!
    </div>
    <div class="captcha">
      <span class="captcha-box"></span>
      <span class="captcha-label">I'm not a robot</span>
      <span class="captcha-mark"></span>
      <div class="captcha-meta">VeriCheck<br>Privacy - Terms</div>
    </div>
  </form>

  <footer class="footer">
    <div class="footer-links">
      <span>B2B Services</span><span class="sep">|</span><span>Aide</span><span class="sep">|</span><span>Conditions générales d'utilisation</span><span class="sep">|</span><span>Respect de la vie privée</span>
    </div>
    <div class="copyright">Copyright Orvane 2022, tous droits réservés.</div>
  </footer>

  <svg class="hero" width="1200" height="600" viewBox="0 0 1200 600">
    <defs>
      <linearGradient id="heroFill" x1="0" y1="0" x2="0.4" y2="1">
        <stop offset="0" stop-color="var(--photo-a)"/>
        <stop offset="0.6" stop-color="#a9774f"/>
        <stop offset="1" stop-color="var(--photo-b)"/>
      </linearGradient>
    </defs>
    <path role="img" aria-label="Photo d'une jeune femme souriante consultant son téléphone en terrasse"
      d="M855 122 C890 118 925 160 960 195 C1010 240 1050 300 1045 360 C1040 440 960 520 830 520 C720 520 665 470 672 420 C680 370 730 320 760 250 C790 180 815 125 855 122 Z"
      fill="url(#heroFill)" stroke="var(--red)" stroke-width="5"/>
  </svg>

  <div class="partner"><span class="partner-dot"></span>www.4747.be</div>
</body>
</html>
```